Gordon Pellbrook Consulting - Web Design Project

We need a web design for my new edgy consulting business specializing in innovation, technology and strategy.

It is our personal goal to turn each client into raving fans by helping them achieve their own business goals and aspirations through assisting them in raising their own innovation and marketing standards.

We provide our personalised and state-of-the-art services to our clients and boards who represent some of the world greatest innovative thinkers.
Updates

Here is some other information which may help shape your thinking.

I've had direct Involvement in the development of the following iPad, iPhone Applications and websites

FarbeyondOzlands.com (TerraLink platform) by Voyage Bureau
http://farbeyondozlands.example.au

Sail Verve by Bright Voyaging
https://apps.example-store.com/au/app/sail-verve/id100000001

uRedlandTR by Travel Territory Board
https://apps.example-store.com/au/app/uredlandtr/id100000002

Wexmoor Trips
http://www.wexmoortrips.example.au

Trek Mapper by Voyage Bureau
http://apps.example-store.com/au/app/trek-mapper/id100000003

Sunward by Sunward Travel Office
https://apps.example-store.com/au/app/sunward/id100000004

Upper Fernridge Valley Route by Visit Coastlands
https://apps.example-store.com/au/app/upper-fernridge-valley-route/id100000005

Wanderer Path by Travel Territory Board and Southern Plains Travel Council
https://apps.example-store.com/au/app/wanderers-path-grand-journey/id100000006

Gordon Pellbrook Consulting (GPC)
November 2012 – Present (8 months)Brisbane, Sydney, Canberra

Gordon’s consults to Small-to-Medium Enterprises (SME) and Government organisations on business strategy, technology strategy, risk mitigation, disruptive technology and innovation in the workplace.

Gordon’s consultancy mantra is that we cannot divorce economic life from cultural life particularly in an era when social capital may be as important as physical capital in business.

Reason: request from designers, I want to see their best efforts

Target Market(s)

35+

Industry/Entity Type

Business

Requirements
Must have
• Please use some of the personal image(s) contained in the zip files which can be downloaded from here

http://filedrop.example/k9Xq2Lm
http://filedrop.example/p4Rt7Vn
http://filedrop.example/z8Hw3Bc
Nice to have
• Black, Sleek design, maybe minimalist. Nice to have a Pixelle for the design. Nice to have it easily ported to Wordpress or be a modified Wordpress template. HTML 5, responsive design

```html
<!DOCTYPE html>
<html lang="en">
<head>
<meta charset="utf-8">
<title>GPC Consulting</title>
<link rel="stylesheet" href="https://fonts.googleapis.com/css2?family=Oswald:wght@300;400;600&family=Poiret+One&family=Open+Sans:wght@400;700&display=swap">
<style>
  :root {
    --black: #000000;
    --brand-blue: #2a5f91;
    --band-blue: #1f4466;
    --rule-blue: #1d3f63;
    --hero-text: #e6e6e6;
    --body-text: #dcdcdc;
    --tagline-ink: #05080c;
    --white: #ffffff;
  }
  * { margin: 0; padding: 0; box-sizing: border-box; }
  html, body { width: 1200px; height: 803px; overflow: hidden; background: var(--black); }
  .page { position: relative; width: 1200px; height: 803px; background: var(--black); overflow: hidden; font-family: Arial, Helvetica, sans-serif; }

  .header-portrait-fade {
    position: absolute; left: 135px; top: 0; width: 175px; height: 108px;
    background: linear-gradient(180deg, #262626 0%, #3a3a3a 60%, #2b2b2b 100%);
    opacity: .7;
  }
  .brand-name {
    position: absolute; left: 328px; top: 62px;
    font-family: 'Oswald', sans-serif; font-weight: 400; font-size: 26px; line-height: 1;
    color: var(--brand-blue); letter-spacing: .5px;
  }

  .main-nav { position: absolute; top: 66px; left: 0; width: 1200px; font-family: 'Oswald', sans-serif; font-weight: 300; font-size: 23px; }
  .main-nav a { position: absolute; color: var(--brand-blue); text-decoration: none; letter-spacing: .3px; }
  .nav-rule { position: absolute; left: 320px; top: 105px; width: 785px; height: 1px; background: var(--rule-blue); }

  .hero { position: absolute; left: 0; top: 108px; width: 1200px; height: 465px; }
  .hero-room {
    position: absolute; inset: 0;
    background:
      radial-gradient(ellipse at 55% 30%, rgba(90,90,90,.6) 0%, rgba(0,0,0,0) 60%),
      linear-gradient(180deg, #1a1a1a 0%, #3a3a3a 45%, #4a4540 75%, #2c2a28 100%);
  }
  .hero-portrait {
    position: absolute; left: 0; top: 0; width: 310px; height: 465px;
    background: linear-gradient(180deg, #2a2e35 0%, #2d3a4d 30%, #2a4a78 65%, #1d3558 100%);
  }
  .hero-copy { position: absolute; left: 409px; top: 106px; width: 745px; }
  .hero-title { font-family: 'Oswald', sans-serif; font-weight: 600; font-size: 36px; color: var(--hero-text); letter-spacing: -.4px; line-height: 1.1; }
  .hero-text { color: var(--body-text); font-size: 15.5px; line-height: 1.2; margin-top: 22px; width: 700px; }
  .hero-text + .hero-text { margin-top: 20px; }

  .tagline-band {
    position: absolute; left: 0; top: 580px; width: 1200px; height: 101px;
    background: var(--band-blue); display: flex; align-items: center; justify-content: center;
  }
  .tagline { font-family: 'Poiret One', sans-serif; font-size: 52px; color: var(--tagline-ink); letter-spacing: 1.5px; }

  .site-footer { position: absolute; left: 0; top: 681px; width: 1200px; height: 122px; color: var(--white); }
  .footer-item { position: absolute; top: 26px; display: flex; align-items: flex-start; gap: 16px; }
  .footer-item svg { flex: none; }
  .footer-heading { font-family: 'Open Sans', sans-serif; font-weight: 700; font-size: 17px; line-height: 1.2; }
  .footer-text { font-family: Arial, Helvetica, sans-serif; font-size: 16.5px; line-height: 1.3; }
  .social-links { display: flex; gap: 8px; margin-top: 3px; font-family: 'Open Sans', sans-serif; font-size: 12px; }
  .copyright { position: absolute; left: 972px; top: 44px; display: flex; align-items: center; gap: 10px; font-size: 16.5px; }
</style>
</head>
<body>
<div class="page">
  <header>
    <div class="header-portrait-fade" role="img" aria-label="Faded portrait of the consultant in the header background"></div>
    <div class="brand-name">GPC Consulting</div>
    <nav class="main-nav">
      <a href="#" style="left:503px">HOME</a>
      <a href="#" style="left:618px">ABOUT</a>
      <a href="#" style="left:740px">SOLUTIONS</a>
      <a href="#" style="left:898px">CLIENTS</a>
      <a href="#" style="left:1031px">CONTACT</a>
    </nav>
    <div class="nav-rule"></div>
  </header>

  <section class="hero">
    <div class="hero-room" role="img" aria-label="Photo of a dim boardroom with a long table and leather chairs"></div>
    <div class="hero-portrait" role="img" aria-label="Portrait of the consultant in a blue suit, arms folded"></div>
    <div class="hero-copy">
      <h1 class="hero-title">Provide personalised and state-of-the-art services</h1>
      <p class="hero-text">Gordon’s consults to Small-to-Medium Enterprises (SME) and Government organisations on business strategy, technology strategy, risk mitigation, disruptive technology and innovation in the workplace.</p>
      <p class="hero-text">Gordon’s consultancy mantra is that we cannot divorce economic life from cultural life particularly in an era when social capital may be as important as physical capital in business.</p>
    </div>
  </section>

  <section class="tagline-band">
    <p class="tagline">Innovation, Technology and Strategy.</p>
  </section>

  <footer class="site-footer">
    <div class="footer-item" style="left:20px">
      <svg width="30" height="46" viewBox="0 0 30 46" aria-hidden="true"><path d="M15 1C7 1 1 7 1 15c0 10 14 30 14 30s14-20 14-30C29 7 23 1 15 1z" fill="#fff"/><rect x="13" y="8" width="4" height="11" fill="#000"/><circle cx="15" cy="23" r="2.2" fill="#000"/></svg>
      <div><div class="footer-heading">Visit</div><div class="footer-text">Kestrel Lane 48<br>Brisbane, Sydney, Canberra</div></div>
    </div>
    <div class="footer-item" style="left:348px">
      <svg width="30" height="46" viewBox="0 0 30 46" aria-hidden="true"><path d="M7 3l6 9-4 4c2 6 5 11 10 15l4-3 6 8-5 5C12 40 2 23 3 8z" fill="#fff"/></svg>
      <div><div class="footer-heading">Call</div><div class="footer-text">T: 07-5550-1420<br>F: 07-5550-1421</div></div>
    </div>
    <div class="footer-item" style="left:670px; top:28px">
      <svg width="58" height="36" viewBox="0 0 58 36" style="margin-top:6px" aria-hidden="true"><rect x="1" y="1" width="56" height="34" fill="#fff"/><path d="M2 2l27 20L56 2M2 34l20-16M56 34L36 18" stroke="#000" stroke-width="2" fill="none"/></svg>
      <div><div class="footer-heading">Contact</div><div class="footer-text">info@gpcmail.example</div>
        <div class="social-links"><span>Friendly</span><span>Chirper</span><span>Circles</span></div></div>
    </div>
    <div class="copyright">
      <svg width="34" height="34" viewBox="0 0 34 34" aria-hidden="true"><circle cx="17" cy="17" r="15" fill="none" stroke="#fff" stroke-width="2.5"/><path d="M22 12a7 7 0 1 0 0 10" fill="none" stroke="#fff" stroke-width="2.5"/></svg>
      <span>2013 GPC Consulting</span>
    </div>
  </footer>
</div>
</body>
</html>
```